TRV PowerPoint

I am looking for a clean, corporate PowerPoint template.

I would like the following:
- title slide
- break slide
- blank slide with title (for graphs or graphics)
- an ending slide.

Target Market(s)

Business professionals, medium to large business clients.

Requirements
Must have
• Must incorporate the TRV logo in either the header or footer

```html
<!DOCTYPE html>
<html lang="en">
<head>
<meta charset="utf-8">
<title>TRV Presentation Template</title>
<link href="https://fonts.googleapis.com/css2?family=PT+Sans:wght@400;700&family=PT+Sans+Narrow:wght@400;700&display=swap" rel="stylesheet">
<style>
  :root {
    --sheet: #c6c6c6;
    --blue-light: #4b92c6;
    --blue-mid: #2f5eab;
    --blue-dark: #1f3d97;
    --navy: #1b2f8f;
    --white: #ffffff;
    --body-text: #666666;
    --rule: #7a7a7a;
    --footer-gray: #545454;
  }
  * { margin: 0; padding: 0; box-sizing: border-box; }
  html, body { width: 1200px; height: 900px; overflow: hidden; background: var(--sheet); }
  body { position: relative; font-family: "PT Sans", sans-serif; }

  .slide { position: absolute; width: 507px; height: 392px; overflow: hidden; }
  .slide--title   { left: 72px;  top: 59px; }
  .slide--content { left: 601px; top: 59px; background: var(--white); }
  .slide--section { left: 72px;  top: 462px; }
  .slide--closing { left: 601px; top: 462px; }

  .blue-field {
    background: linear-gradient(to top right, var(--blue-light) 0%, var(--blue-mid) 55%, var(--blue-dark) 100%);
  }

  /* Brand lockup */
  .brand { position: absolute; display: flex; align-items: center; gap: 6px; white-space: nowrap; }
  .brand__mark { display: block; background: currentColor; }
  .brand__name { font-family: "PT Sans", sans-serif; font-weight: 700; letter-spacing: 0.04em; text-transform: uppercase; }
  .brand--navy { color: var(--navy); }
  .brand--white { color: var(--white); }

  /* Title slide */
  .title-slide__intro { position: absolute; right: 32px; top: 150px; text-align: right; color: var(--white); }
  .title-slide__welcome { font-family: "PT Sans Narrow", sans-serif; font-weight: 700; font-size: 27px; line-height: 32px; }
  .title-slide__headline { font-family: "PT Sans Narrow", sans-serif; font-weight: 400; font-size: 27px; line-height: 32px; }
  .title-slide__meta { font-size: 14px; margin-top: 10px; }
  .title-slide__band {
    position: absolute; left: 0; top: 299px; width: 100%; height: 61px;
    background: var(--white); border-top: 2px solid #8a8a8a; border-bottom: 2px solid #8a8a8a;
  }
  .title-slide__band .brand { right: 23px; top: 14px; }
  .title-slide__band .brand__mark { width: 22px; height: 22px; }
  .title-slide__band .brand__name { font-size: 19px; }

  /* Content slide */
  .content-slide__header {
    position: absolute; left: 0; top: 0; width: 100%; height: 42px;
    background: linear-gradient(to right, #2f62ae 0%, #4b92c6 35%, #3a73b8 70%, var(--navy) 100%);
    border-bottom: 2px solid #7f7f7f;
  }
  .content-slide__title {
    position: absolute; left: 32px; top: 11px; color: var(--white);
    font-weight: 700; font-size: 18px; line-height: 20px; letter-spacing: 0.01em;
  }
  .content-slide__chart { position: absolute; left: 31px; top: 178px; }
  .content-slide__copy { position: absolute; left: 239px; top: 82px; width: 233px; }
  .content-slide__copy p {
    font-size: 8.8px; line-height: 18px; color: var(--body-text); text-align: justify; margin-bottom: 18px;
  }
  .content-slide__footer-rule { position: absolute; left: 21px; top: 357px; width: 465px; height: 1px; background: var(--rule); }
  .content-slide__footer .brand { left: 21px; top: 363px; }
  .content-slide__footer .brand__mark { width: 11px; height: 11px; }
  .content-slide__footer .brand__name { font-size: 9.5px; }
  .content-slide__page { position: absolute; right: 21px; top: 364px; font-size: 7px; color: var(--body-text); }

  /* Section slide */
  .section-slide__title {
    position: absolute; right: 13px; top: 180px; color: var(--white);
    font-family: "PT Sans Narrow", sans-serif; font-size: 22px; line-height: 24px;
  }
  .section-slide__footer {
    position: absolute; left: 0; top: 362px; width: 100%; height: 30px;
    background: var(--footer-gray); border-top: 2px solid var(--white);
  }
  .section-slide__footer .brand { left: 17px; top: 7px; }
  .section-slide__footer .brand__mark { width: 11px; height: 11px; }
  .section-slide__footer .brand__name { font-size: 9.5px; }

  /* Closing slide */
  .closing-slide__title {
    position: absolute; left: 0; width: 100%; top: 184px; text-align: center; padding-right: 16px; color: var(--white);
    font-family: "PT Sans Narrow", sans-serif; font-size: 22px; line-height: 24px;
  }
  .closing-slide .brand { left: 50%; transform: translateX(-50%); top: 338px; }
  .closing-slide .brand__mark { width: 18px; height: 18px; }
  .closing-slide .brand__name { font-size: 15px; }
</style>
</head>
<body>

  <!-- Title slide -->
  <section class="slide slide--title blue-field">
    <div class="title-slide__intro">
      <h1 class="title-slide__welcome">WELCOME</h1>
      <p class="title-slide__headline">TO OUR PRESENTATION</p>
      <p class="title-slide__meta">Birmingham, August 25, 2013</p>
    </div>
    <div class="title-slide__band">
      <div class="brand brand--navy">
        <span class="brand__mark"></span>
        <span class="brand__name">TRV Tessa Rowe Ventures</span>
      </div>
    </div>
  </section>

  <!-- Content slide with chart -->
  <section class="slide slide--content">
    <header class="content-slide__header">
      <h2 class="content-slide__title">PRESENTATION TITLE</h2>
    </header>

    <svg class="content-slide__chart" width="220" height="150" viewBox="0 0 220 150" role="img" aria-label="Pie chart">
      <defs>
        <radialGradient id="pie-shadow" cx="50%" cy="50%" r="50%">
          <stop offset="0%" stop-color="#000" stop-opacity="0.35"/>
          <stop offset="100%" stop-color="#000" stop-opacity="0"/>
        </radialGradient>
      </defs>
      <ellipse cx="110" cy="119" rx="100" ry="6" fill="url(#pie-shadow)"/>
      <path d="M22,70 A88,62 0 0 0 198,70 L198,86 A88,62 0 0 1 22,86 Z" fill="#2e2e2e"/>
      <path d="M110,70 L110,8 A88,62 0 0 1 154,123.7 Z" fill="#5a5a5a"/>
      <path d="M110,70 L154,123.7 A88,62 0 0 1 27.3,91.2 Z" fill="#666666"/>
      <path d="M110,70 L27.3,91.2 A88,62 0 0 1 33.8,39 Z" fill="#7a7a7a"/>
      <path d="M110,70 L33.8,39 A88,62 0 0 1 66,16.3 Z" fill="#0d63a8"/>
      <path d="M110,70 L66,16.3 A88,62 0 0 1 110,8 Z" fill="#5bbfdb"/>
    </svg>

    <div class="content-slide__copy">
      <p>Lorem ipsum dolor sit amet, consectetur adipisicing elit, sed do eiusmod tempor incididunt ut labore et dolore magna aliqua. Ut enim ad minim veniam, quis nostrud exercitation ullamco laboris nisi ut aliquip ex ea commodo consequat. Duis aute irure dolor in reprehenderit in voluptate velit esse cillum dolore eu fugiat nulla pariatur.</p>
      <p>Lorem ipsum dolor sit amet, consectetur adipisicing elit, sed do eiusmod tempor incididunt ut labore et dolore magna aliqua. Ut enim ad minim veniam, quis nostrud exercitation ullamco laboris nisi ut aliquip ex ea commodo consequat. Duis aute irure dolor in reprehenderit in voluptate velit esse cillum dolore eu fugiat nulla</p>
    </div>

    <footer class="content-slide__footer">
      <div class="content-slide__footer-rule"></div>
      <div class="brand brand--navy">
        <span class="brand__mark"></span>
        <span class="brand__name">TRV Tessa Rowe Ventures</span>
      </div>
      <span class="content-slide__page">2</span>
    </footer>
  </section>

  <!-- Section break slide -->
  <section class="slide slide--section blue-field">
    <h2 class="section-slide__title">SECTION TITLE</h2>
    <footer class="section-slide__footer">
      <div class="brand brand--white">
        <span class="brand__mark"></span>
        <span class="brand__name">TRV Tessa Rowe Ventures</span>
      </div>
    </footer>
  </section>

  <!-- Closing slide -->
  <section class="slide slide--closing closing-slide blue-field">
    <h2 class="closing-slide__title">THANK YOU</h2>
    <div class="brand brand--white">
      <span class="brand__mark"></span>
      <span class="brand__name">TRV Tessa Rowe Ventures</span>
    </div>
  </section>

</body>
</html>
```